Logo is done, need templates now

I want to be able to have an email template, same for word documents, powerpoint etc. I have the logo, now I need all the pieces for appearance in correspondence and marketing

Target Market(s)

Professional Advisors and Wealthy Clients

Font styles to use
Serif

Requirements
Must have
• I want to be able to do word documents and email them with letterhead. I need great email signatures. I need similar formatting for the word documents to be flexible to add to powerpoint and other presentations.

```html
<!DOCTYPE html>
<html lang="en">
<head>
<meta charset="utf-8">
<title>Larkmere Capital — Email Signature</title>
<link href="https://fonts.googleapis.com/css2?family=Roboto+Condensed:wght@400;700&display=swap" rel="stylesheet">
<style>
  :root {
    --page: #ffffff;
    --charcoal: #2e2d2d;
    --gold: #c9a36a;
    --ink: #333333;
    --light: #ffffff;
  }
  html, body {
    margin: 0;
    padding: 0;
    width: 1200px;
    height: 1041px;
    overflow: hidden;
    background: var(--page);
    font-family: "Roboto Condensed", Arial, sans-serif;
  }
  .signature {
    position: absolute;
    left: 42px;
    top: 380px;
    width: 1115px;
    height: 280px;
  }
  .contact-band {
    position: absolute;
    left: 0;
    top: 72px;
    width: 1115px;
    height: 124px;
    background: var(--charcoal);
  }
  .brand-frame {
    position: absolute;
    left: 48px;
    top: -7px;
    width: 314px;
    height: 170px;
    background: var(--light);
  }
  .brand-tile {
    position: absolute;
    left: 55px;
    top: 0;
    width: 301px;
    height: 156px;
    background: var(--charcoal);
    display: flex;
    align-items: center;
    justify-content: center;
  }
  .brand-name {
    color: var(--gold);
    font-weight: 400;
    font-size: 21px;
    letter-spacing: 4px;
    margin-top: 40px;
  }
  .person {
    position: absolute;
    left: 405px;
    top: 2px;
    color: var(--ink);
  }
  .person-name {
    font-weight: 700;
    font-size: 24px;
    line-height: 28px;
  }
  .person-role {
    font-size: 18px;
    line-height: 24px;
  }
  .details {
    position: absolute;
    top: 120px;
    display: flex;
    align-items: center;
    color: var(--light);
    font-size: 14px;
    line-height: 21px;
  }
  .details .col { padding: 0 20px; }
  .details .col + .col { border-left: 1px solid #8a8580; }
  .details .col:first-child { padding-left: 0; }
  .label { color: var(--gold); }
  .web { color: var(--gold); font-weight: 700; }
  .details { left: 405px; }
  .social {
    position: absolute;
    left: 1034px;
    top: 113px;
    display: grid;
    grid-template-columns: 20px 20px;
    gap: 10px 7px;
  }
  .social span {
    width: 20px;
    height: 20px;
    border-radius: 3px;
    background: var(--gold);
  }
  .disclaimer {
    position: absolute;
    left: 55px;
    top: 210px;
    width: 1060px;
    color: var(--ink);
    font-size: 12px;
    line-height: 16.5px;
    letter-spacing: -0.2px;
    margin: 0;
  }
</style>
</head>
<body>
  <section class="signature">
    <div class="contact-band"></div>
    <div class="brand-frame"></div>
    <div class="brand-tile"><span class="brand-name">LARKMERE CAPITAL</span></div>
    <div class="person">
      <div class="person-name">JORDAN PELLEW</div>
      <div class="person-role">General Manager</div>
    </div>
    <div class="details">
      <div class="col">2280-88 AVENUE<br>CALGARY AB T3K 0L4</div>
      <div class="col"><span class="label">T:</span> 888-555-0142<br><span class="label">F:</span> 888-555-0178</div>
      <div class="col">HELLO@LARKMERECAPITAL.CA<br><span class="web">WWW.LARKMERECAPITAL.CA</span></div>
    </div>
    <div class="social" aria-label="Social links">
      <span></span><span></span><span></span><span></span>
    </div>
    <p class="disclaimer">The content of this email is confidential and intended for the recipient specified in message only. If you received this message by mistake, please reply to this message and follow with its deletion, so that we can ensure such a mistake does not occur in the future. In LARKMERE CAPITAL we put the security of the client at a high priority. Therefore, we have put efforts into ensuring that the message is error and virus-free. Unfortunately, full security of the email cannot be ensured as, despite our efforts, the data included in emails could be infected, intercepted, or corrupted. Therefore, the recipient should check the email for threats with proper software, as the sender does not accept liability for any damage inflicted by viewing the content of this email.</p>
  </section>
</body>
</html>
```